Postcard Design

We provide humorous speechwriting and presentation coaching services, primarily for the wedding market (best man, father of the bride, maid of honor). We'd like a design that incoporates the blue and white logo colors into a nice overall design, with the pitch:
"Use the power of humor to deliver the BEST speech of your life!"
Target Market(s)
Wedding market (best man, bride/groom)
Industry/Entity Type
Wedding
Requirements
Must have
- Bulletpoints for services provided:
- Speechwriting
- Presentation Coaching
- Emcee & Officiant Services
Listing of benefits provided:
- Conquer stage fright
- Deliver your speech like a pro
- Be funny AND tactful
- Leave them wanting more
Contact info -
Trent Halvorsen
Trent@QuipCraftly.com
www.QuipCraftly.com
Testimonial quotes:
"People are STILL raving about that speech at our wedding. Thanks Quip Craftly!"
- Dana & Paul Fenwick, Baltimore, MD
"With the help of Quip Craftly, my best man speech brought down the house!"
- Mark Delahunt, Melville, NY

```html
<!DOCTYPE html>
<html lang="en">
<head>
<meta charset="utf-8">
<title>Quip Craftly Postcard</title>
<link rel="stylesheet" href="https://fonts.googleapis.com/css2?family=Lato:wght@400;700;900&family=Kalam:wght@400;700&family=Tinos:ital@0;1&display=swap">
<style>
  :root {
    --navy: #1d2f6f;
    --navy-deep: #14215a;
    --navy-light: #34489a;
    --white: #ffffff;
    --paper: #f7f8fa;
    --bar: #eef0f4;
    --sky: #cfe0ec;
    --sea: #8fb6c9;
    --sand: #e8e2d8;
    --ink-faint: #e6e6e6;
    --line: #4a4a4a;
    --backdrop: #1c1c1c;
  }
  * { box-sizing: border-box; margin: 0; padding: 0; }
  html, body {
    width: 797px; height: 1200px; overflow: hidden;
    background: var(--backdrop);
  }
  .postcard {
    position: absolute;
    width: 702px;
    background: var(--white);
    overflow: hidden;
  }
  /* Front */
  .postcard--front { left: 48px; top: 40px; height: 540px; }
  .front-art { position: absolute; inset: 0; }
  .front-url {
    position: absolute; right: 28px; top: 22px;
    font: 400 24px "Lato", sans-serif; color: var(--navy);
  }
  .front-pitch {
    position: absolute; left: 26px; top: 448px;
    font-family: "Kalam", cursive; color: var(--white); line-height: 1.2;
  }
  .front-pitch .line-1 { font-size: 21px; display: block; }
  .front-pitch .line-2 { font-size: 28px; display: block; }
  .brand-seal {
    position: absolute; left: 528px; top: 375px;
    width: 150px; height: 150px; border-radius: 50%;
    background: var(--navy);
    display: flex; align-items: center; justify-content: center; text-align: center;
    font: 700 24px/1.05 "Lato", sans-serif; color: var(--white);
    letter-spacing: 0.5px;
  }
  /* Back */
  .postcard--back { left: 44px; top: 628px; height: 530px; }
  .info-panel {
    position: absolute; left: 0; top: 0; width: 345px; height: 100%;
    background: linear-gradient(90deg, var(--navy-light), var(--navy) 60%, var(--navy-deep));
  }
  .info-panel::after {
    content: ""; position: absolute; right: 0; top: 0; width: 8px; height: 100%;
    background: var(--navy-deep);
  }
  .section-heading {
    position: absolute; left: 0; width: 310px; height: 40px;
    background: linear-gradient(180deg, var(--white), var(--bar));
    font: 400 24px/40px "Lato", sans-serif; color: var(--navy);
    padding-left: 30px; letter-spacing: 0.3px;
  }
  .check-list {
    position: absolute; left: 34px; list-style: none;
    font: 400 17px/21px "Tinos", serif; color: var(--white);
  }
  .check-list li { display: flex; align-items: center; gap: 8px; }
  .check-list svg { width: 10px; height: 10px; flex: none; }
  .testimonials {
    position: absolute; left: 34px; top: 360px; width: 290px;
    font: italic 12px/15px "Tinos", serif; color: var(--white); list-style: none;
  }
  .testimonials li { position: relative; padding-left: 12px; margin-bottom: 10px; }
  .testimonials li::before {
    content: ""; position: absolute; left: 0; top: 3px;
    width: 8px; height: 8px; border-radius: 50%; background: var(--white);
  }
  .testimonials cite { display: block; padding-left: 4px; }
  .contact-strip { position: absolute; left: 0; bottom: 0; width: 702px; height: 70px; }
  .contact-email {
    position: absolute; left: 70px; bottom: 8px;
    font: 400 19px "Tinos", serif; color: var(--navy-deep);
  }
  .contact-icon { position: absolute; left: 36px; bottom: 12px; width: 22px; height: 18px; }
  .stamp-box {
    position: absolute; left: 618px; top: 19px; width: 70px; height: 90px;
    border: 2px solid var(--line);
  }
  .faint-seal {
    position: absolute; left: 406px; top: 157px; width: 270px; height: 270px;
    border-radius: 50%; border: 3px solid var(--ink-faint);
    display: flex; align-items: center; justify-content: center; text-align: center;
    font: 700 36px/1.05 "Lato", sans-serif; color: var(--ink-faint);
  }
  .address-line {
    position: absolute; left: 436px; width: 252px; height: 0;
    border-top: 1.5px solid var(--line);
  }
</style>
</head>
<body>

<section class="postcard postcard--front">
  <svg class="front-art" width="702" height="540" viewBox="0 0 702 540">
    <defs>
      <linearGradient id="photoTone" x1="0" y1="0" x2="0" y2="1">
        <stop offset="0" stop-color="#f4f7fa"/>
        <stop offset="0.25" stop-color="var(--sky)"/>
        <stop offset="0.5" stop-color="var(--sea)"/>
        <stop offset="1" stop-color="var(--sand)"/>
      </linearGradient>
      <linearGradient id="bandTone" x1="0" y1="0" x2="1" y2="0">
        <stop offset="0" stop-color="var(--navy)"/>
        <stop offset="0.5" stop-color="var(--navy-light)"/>
        <stop offset="1" stop-color="var(--navy-deep)"/>
      </linearGradient>
    </defs>
    <rect width="702" height="440" fill="url(#photoTone)" role="img" aria-label="Photo of a smiling bride and groom embracing on a beach"/>
    <path d="M0,415 Q360,440 702,255 L702,540 L0,540 Z" fill="var(--paper)"/>
    <path d="M0,392 Q360,420 702,238 L702,262 Q370,445 0,418 Z" fill="var(--navy)"/>
    <path d="M0,422 C200,445 430,420 612,330 C560,420 536,480 530,540 L0,540 Z" fill="url(#bandTone)"/>
  </svg>
  <div class="front-url">www.QuipCraftly.com</div>
  <p class="front-pitch">
    <span class="line-1">Use the power of humor to deliver</span>
    <span class="line-2">the BEST speech of your life!</span>
  </p>
  <div class="brand-seal">QUIP<br>CRAFTLY</div>
</section>

<section class="postcard postcard--back">
  <div class="info-panel"></div>

  <h2 class="section-heading" style="top:17px">SERVICES PROVIDED</h2>
  <ul class="check-list" style="top:64px">
    <li><svg viewBox="0 0 10 10"><rect x="0.5" y="0.5" width="9" height="9" fill="none" stroke="#fff"/><path d="M2 5 L4.5 7.5 L9.5 1" fill="none" stroke="#fff" stroke-width="1.4"/></svg>Speechwriting</li>
    <li><svg viewBox="0 0 10 10"><rect x="0.5" y="0.5" width="9" height="9" fill="none" stroke="#fff"/><path d="M2 5 L4.5 7.5 L9.5 1" fill="none" stroke="#fff" stroke-width="1.4"/></svg>Presentation Coaching</li>
    <li><svg viewBox="0 0 10 10"><rect x="0.5" y="0.5" width="9" height="9" fill="none" stroke="#fff"/><path d="M2 5 L4.5 7.5 L9.5 1" fill="none" stroke="#fff" stroke-width="1.4"/></svg>Emcee &amp; Officiant Services</li>
  </ul>

  <h2 class="section-heading" style="top:140px">BENEFITS PROVIDED</h2>
  <ul class="check-list" style="top:200px">
    <li><svg viewBox="0 0 10 10"><rect x="0.5" y="0.5" width="9" height="9" fill="none" stroke="#fff"/><path d="M2 5 L4.5 7.5 L9.5 1" fill="none" stroke="#fff" stroke-width="1.4"/></svg>Conquer stage fright</li>
    <li><svg viewBox="0 0 10 10"><rect x="0.5" y="0.5" width="9" height="9" fill="none" stroke="#fff"/><path d="M2 5 L4.5 7.5 L9.5 1" fill="none" stroke="#fff" stroke-width="1.4"/></svg>Deliver your speech like a pro</li>
    <li><svg viewBox="0 0 10 10"><rect x="0.5" y="0.5" width="9" height="9" fill="none" stroke="#fff"/><path d="M2 5 L4.5 7.5 L9.5 1" fill="none" stroke="#fff" stroke-width="1.4"/></svg>Be funny AND tactful</li>
    <li><svg viewBox="0 0 10 10"><rect x="0.5" y="0.5" width="9" height="9" fill="none" stroke="#fff"/><path d="M2 5 L4.5 7.5 L9.5 1" fill="none" stroke="#fff" stroke-width="1.4"/></svg>Leave them wanting more</li>
  </ul>

  <h2 class="section-heading" style="top:296px">TESTIMONIAL QUOTES</h2>
  <ul class="testimonials">
    <li>“People are STILL raving about that speech at our wedding. Thanks Quip Craftly!”<cite>- Dana &amp; Paul Fenwick, Baltimore, MD</cite></li>
    <li>“With the help of Quip Craftly, my best man speech brought down the house!”<cite>- Mark Delahunt, Melville, NY</cite></li>
  </ul>

  <svg class="contact-strip" viewBox="0 0 702 70" preserveAspectRatio="none">
    <path d="M0,0 Q200,22 380,60 L380,70 L0,70 Z" fill="var(--white)"/>
    <path d="M0,0 Q200,22 380,60" fill="none" stroke="var(--navy)" stroke-width="3"/>
  </svg>
  <svg class="contact-icon" viewBox="0 0 22 18">
    <rect x="1" y="3" width="20" height="14" fill="#fff" stroke="#777" stroke-width="1.2"/>
    <path d="M1 3 L11 11 L21 3" fill="none" stroke="#777" stroke-width="1.2"/>
  </svg>
  <p class="contact-email">Trent@QuipCraftly.com</p>

  <div class="faint-seal">QUIP<br>CRAFTLY</div>
  <div class="stamp-box"></div>
  <div class="address-line" style="top:260px"></div>
  <div class="address-line" style="top:310px"></div>
  <div class="address-line" style="top:362px"></div>
</section>

</body>
</html>
```